Stationary pack for BrightNest

BrightNest is a recently establish Solar brokerage company based in Australia. We have a number of sales staff who provide advice and guidance to both residential and commercial customers regarding solar systems (solar hot water and solar panels.)

In addition to our brokerage services we are also developing software for the solar industry, which will be used to automate the solar system install process. This system will be used by other companies in the solar industry including installers, wholesalers and government departments.

We are after a stationary pack that consists of the following: Business cards, compliments slip and letter head.

The EPS, AI, PNG etc files for the logo are attached.

For the business card:
The name and logo of the company need to be clearly visible. On the back of the business cards, we would like the logo. I am happy for you to split the image part of the logo from the text if you think it would look better a different way.

I would like the business cards to be easily readable with the following information on the front:
Name
(Please leave room for titles for the future – eg Sales Advisor.)
Mobile
Office
Email
Address
ABN

Letter heads:
I would prefer the address to be at the top

Compliments slips:
Only need to be one sided

Target Market(s)

BrightNest provides services to both residential and commercial customers. Our customers will be environmentally conscious.

Industry/Entity Type

Residential

Requirements
Must have
• Business cards must have the logo on the back.

```html
<!DOCTYPE html>
<html lang="en">
<head>
<meta charset="utf-8">
<title>BrightNest Stationery Pack</title>
<link rel="stylesheet" href="https://fonts.googleapis.com/css2?family=Montserrat:wght@700&family=Arimo:wght@400;700&display=swap">
<style>
  :root {
    --bg: #000000;
    --paper: #ffffff;
    --green: #5aa630;
    --orange: #f6a21a;
    --blue: #2a5d9f;
    --grey: #6b6b6b;
    --rule: #9a9a9a;
  }
  * { margin: 0; padding: 0; box-sizing: border-box; }
  html, body { width: 1200px; height: 900px; overflow: hidden; background: var(--bg); }
  body { position: relative; font-family: "Arimo", Arial, sans-serif; color: var(--grey); }

  .sheet { position: absolute; background: var(--paper); overflow: hidden; }
  .edge { position: absolute; left: 0; top: 0; bottom: 0; width: 14px; background: var(--orange); }
  .edge::before { content: ""; position: absolute; left: 0; top: 0; width: 100%; height: var(--green-h); background: var(--green); }

  .brand { position: absolute; display: flex; align-items: center; gap: 8px;
    font-family: "Montserrat", Arial, sans-serif; font-weight: 700; color: var(--green); letter-spacing: -0.5px; }
  .brand .dot { border-radius: 50%; background: var(--orange); flex: none; }

  .divider { position: absolute; width: 1px; background: var(--rule); }
  .address { position: absolute; font-size: 9px; line-height: 11px; color: var(--grey); }

  /* Letterhead */
  .letterhead { left: 64px; top: 80px; width: 522px; height: 740px; --green-h: 90px; }
  .letterhead .brand { left: 36px; top: 30px; font-size: 22px; }
  .letterhead .brand .dot { width: 26px; height: 26px; }
  .letterhead .divider { left: 352px; top: 28px; height: 50px; }
  .letterhead .address { left: 368px; top: 32px; }

  /* Business cards */
  .card { top: 124px; width: 224px; height: 124px; border-radius: 10px; }
  .card-front { left: 666px; }
  .card-back { left: 900px; }
  .card-front .person { position: absolute; left: 28px; top: 12px; }
  .person .name { font-size: 8px; font-weight: 700; color: var(--green); }
  .person .title { font-size: 6px; color: var(--grey); margin-top: 2px; }
  .card-front .details { position: absolute; left: 28px; top: 40px; font-size: 6px; line-height: 10px; }
  .card-front .stripe { position: absolute; left: 0; right: 0; bottom: 0; height: 6px; background: var(--orange); }
  .card-back .brand { right: 18px; top: 38px; font-size: 15px; gap: 5px; }
  .card-back .brand .dot { width: 16px; height: 16px; }
  .card-back .web { position: absolute; right: 18px; bottom: 10px; font-size: 5px; }
  .card-back .stripe { position: absolute; left: 0; right: 0; bottom: 0; height: 6px;
    background: linear-gradient(to right, var(--orange) 0 70%, var(--green) 70% 100%); }

  /* Compliments slip */
  .slip { left: 634px; top: 290px; width: 522px; height: 246px; --green-h: 66px; }
  .slip .brand { left: 22px; top: 20px; font-size: 17px; gap: 6px; }
  .slip .brand .dot { width: 22px; height: 22px; }
  .slip .divider { left: 168px; top: 16px; height: 32px; }
  .slip .address { left: 180px; top: 18px; }
  .slip .greeting { position: absolute; left: 22px; top: 74px; font-size: 16px; font-weight: 700; color: var(--blue); }

  /* Envelope */
  .envelope { left: 634px; top: 560px; width: 522px; height: 246px; --green-h: 76px; }
  .envelope .lockup { position: absolute; left: 0; right: 0; top: 62px; text-align: center; }
  .envelope .dot-mark { width: 42px; height: 42px; border-radius: 50%; background: var(--orange); margin: 0 auto 10px; }
  .envelope .wordmark { font-family: "Montserrat", Arial, sans-serif; font-weight: 700; font-size: 34px;
    color: var(--green); letter-spacing: -1px; line-height: 1; }
  .envelope .web { font-size: 15px; color: var(--grey); margin-top: 6px; }
</style>
</head>
<body>

  <section class="sheet letterhead" aria-label="Letterhead">
    <div class="edge"></div>
    <div class="brand"><span class="dot"></span>brightnest</div>
    <div class="divider"></div>
    <address class="address">48 Wattle Lane<br>Newcastle, NSW 2300<br>Phone: 1300 555 012<br>Email: hello@brightnest.com.au</address>
  </section>

  <section class="sheet card card-front" aria-label="Business card front">
    <div class="person">
      <p class="name">Sam Carter</p>
      <p class="title">Sales Advisor</p>
    </div>
    <div class="details">
      <p>48 Wattle Lane, Newcastle</p>
      <p>NSW 2300 Australia</p>
      <p>M: 0400 555 012</p>
      <p>O: 1300 555 012</p>
      <p>E: sam@brightnest.com.au</p>
      <p>ABN 12 345 678 901</p>
    </div>
    <div class="stripe"></div>
  </section>

  <section class="sheet card card-back" aria-label="Business card back">
    <div class="brand"><span class="dot"></span>brightnest</div>
    <p class="web">www.brightnest.com.au</p>
    <div class="stripe"></div>
  </section>

  <section class="sheet slip" aria-label="Compliments slip">
    <div class="edge"></div>
    <div class="brand"><span class="dot"></span>brightnest</div>
    <div class="divider"></div>
    <address class="address">BrightNest Pty Ltd<br>48 Wattle Lane 2300<br>NSW, Australia</address>
    <h2 class="greeting">With Compliment</h2>
  </section>

  <section class="sheet envelope" aria-label="Envelope">
    <div class="edge"></div>
    <div class="lockup">
      <div class="dot-mark"></div>
      <p class="wordmark">brightnest</p>
      <p class="web">www.brightnest.com.au</p>
    </div>
  </section>

</body>
</html>
```